依頼詳細
現在のホームページのデザインから、最新のデザインへのリニューアルを考えております。スマートフォンへの対応も重要と考えレスポンシブデザインを希望します。

お客様が大変気に入っているデザインがこのサイト(https://www.hoshizora-games.jp/products/kirari/)です。下にスクロールするとギミックがあるものですが、あまり大きな変化はないものを希望します。

現在のホームページは、かなり時間をかけ社内で撮影、レイアウト、構築をおこなっておりました。

参考サイト(https://www.hoshizora-games.jp/products/kirari/)のような先進的なデザインをプロにお願いしたく今回コンペを開催いたします。

画像等は、有料素材サイトなどからのご提案もお願いいたします。
会社のロゴは、添付の会社案内のロゴでお願いします。
サイトURL
http://www.tsubakibuilds.co.jp
ページ数
1ページ
希望イメージ
シンプル 複雑
単色 カラフル
暗い 明るい
日常 高級
遊び心 厳粛
未来的 伝統的
女性的 男性的
希望する色
青系、水色系
納品ファイル
• 高解像度JPG (.jpg)
• イラストレーター形式 (.ai)
• フォトショップ形式 (.psd)
補足説明
レスポンシブデザインもご提案をお願いいたします。

お客様の社内で投票を行いました。
一番に選ばれました。リクルートをメインにしたホームページリニューアルでしたので若い方の支持を重要視しました。
素晴らしいデザインありがとうございました。
今後ともよろしくお願いいたします。

複数のご提案ありがとうございました。
今後もデザインコンペを行ってまいりますので、よろしくお願いいたします。

```html
<!DOCTYPE html>
<html lang="ja">
<head>
<meta charset="utf-8">
<title>椿ビルズ株式会社</title>
<link href="https://fonts.googleapis.com/css2?family=Noto+Sans+JP:wght@400;500;700;900&family=Oswald:wght@400;500&display=swap" rel="stylesheet">
<style>
:root{
  --teal:#1fb6c1;
  --teal-dark:#0e8e98;
  --teal-deep:#0a6f78;
  --black:#0b0b0b;
  --ink:#222;
  --white:#fff;
  --footer:#3b3b3b;
  --muted:#9a9a9a;
}
*{box-sizing:border-box;margin:0;padding:0}
html,body{width:1200px;height:4276px;overflow:hidden}
body{font-family:"Noto Sans JP",sans-serif;color:var(--ink);background:var(--white)}
.en{font-family:"Oswald",sans-serif;letter-spacing:.08em}

/* header + hero */
.hero{position:relative;height:592px;background:linear-gradient(180deg,#2b2620 0%,#5a4330 45%,#2a221d 100%)}
.hero-photo{position:absolute;inset:0;background:radial-gradient(ellipse at 50% 55%,#b58b52 0%,#5b412b 40%,#1e1915 80%)}
.site-header{position:absolute;top:0;left:0;right:0;height:112px;background:rgba(0,0,0,.55);display:flex;align-items:center;justify-content:space-between;padding:0 40px}
.nav{display:flex;gap:54px;list-style:none;color:var(--white);font-size:14px}
.brand{position:absolute;left:50%;transform:translateX(-50%);top:14px;text-align:center;color:var(--white)}
.brand-tag{font-size:11px;letter-spacing:.1em}
.brand-name{display:flex;align-items:center;gap:10px;font-size:26px;font-weight:700;margin-top:4px}
.brand-mark{width:22px;height:22px;border-radius:50%;background:var(--white)}
.tel{position:absolute;right:40px;top:14px;color:var(--white);font-size:30px;font-weight:500}
.tel small{font-size:16px;margin-right:6px}
.header-nav-right{position:absolute;right:40px;bottom:18px}
.header-nav-left{position:absolute;left:160px;bottom:18px}
.hero-copy{position:absolute;left:50%;top:164px;transform:translateX(-50%);width:344px;border:2px solid var(--teal);background:rgba(0,0,0,.55);padding:22px 26px;color:var(--white);text-align:center}
.hero-copy h1{font-size:28px;font-weight:700;letter-spacing:.1em;margin-bottom:14px}
.hero-copy p{font-size:12px;line-height:1.9;color:#bdeff2;text-align:left}

/* info bar */
.info{height:108px;background:var(--black);display:flex;align-items:center;justify-content:center;gap:0}
.info-label{background:#1c1c1c;color:var(--white);font-size:13px;padding:14px 20px;width:170px}
.info-body{background:#1c1c1c;color:#ccc;font-size:13px;padding:14px 20px;width:590px;border-left:1px solid #333}
.info-body span{margin-right:20px}
.info-btn{background:var(--teal);color:var(--white);font-size:13px;padding:14px 22px}

/* grid */
.grid{display:grid;grid-template-columns:1fr 1fr}
.cell{position:relative;height:340px}
.cell.tall{height:390px}
.photo{display:block}
.panel{background:var(--teal);color:var(--white);display:flex;flex-direction:column;align-items:center;justify-content:center}
.panel-lead{font-size:15px;margin-bottom:10px}
.panel-label{background:var(--teal-deep);width:300px;text-align:center;font-size:13px;padding:4px 0}
.panel-title{width:300px;border:2px solid var(--white);text-align:center;font-size:26px;font-weight:700;padding:10px 0;letter-spacing:.08em}
.more{margin-top:44px;width:300px;border:2px solid var(--white);text-align:center;font-size:14px;padding:9px 0;position:relative}
.more::after{content:"";position:absolute;right:18px;top:50%;width:8px;height:8px;border-top:2px solid currentColor;border-right:2px solid currentColor;transform:translateY(-50%) rotate(45deg)}

/* access */
.access{height:710px;background:var(--black);color:var(--white);padding-top:80px}
.sec-head{text-align:center}
.sec-head .en{color:var(--teal);font-size:15px}
.sec-head h2{display:inline-block;font-size:30px;font-weight:700;padding:6px 30px;border-top:2px solid var(--teal);border-bottom:2px solid var(--teal);margin-top:4px}
.map{width:1056px;height:250px;margin:50px auto 0;background:linear-gradient(135deg,#dfe7d7,#eef0ea 50%,#c9dbe8)}
.access-foot{width:1056px;margin:26px auto 0;display:flex;justify-content:flex-end;align-items:center;gap:40px;font-size:13px}
.btn-dark{border:2px solid var(--white);width:210px;padding:8px 0;text-align:center;position:relative}
.btn-dark::after{content:"";position:absolute;right:14px;top:50%;width:7px;height:7px;border-top:2px solid #fff;border-right:2px solid #fff;transform:translateY(-50%) rotate(45deg)}

/* character */
.chara{height:740px;background:var(--white);padding-top:88px}
.chara .sec-head h2{color:var(--ink)}
.chara-banner{width:1056px;height:340px;margin:56px auto 0;display:flex;border:3px solid #111}
.chara-a{flex:1;background:#f4d21f}
.chara-b{flex:1;background:#f06bb5}
.chara .more{margin:40px auto 0;width:210px;color:var(--teal);border-color:var(--teal);background:#e9f8fa;font-size:13px}

/* footer */
.site-footer{height:376px;background:var(--footer);color:#ddd;padding-top:40px}
.foot-nav{display:flex;justify-content:center;gap:60px;font-size:12px}
.foot-nav ul{list-style:none;line-height:2}
.foot-nav ul li+li{color:var(--muted);font-size:11px}
.foot-brand{text-align:center;margin-top:40px;color:var(--white)}
.foot-brand .brand-name{justify-content:center;font-size:24px}
.foot-brand .tel-foot{font-size:26px;margin-top:6px}
.copy{text-align:center;font-size:10px;color:var(--muted);margin-top:30px}
</style>
</head>
<body>

<section class="hero">
  <div class="hero-photo" role="img" aria-label="トンネル工事現場に立つ作業員の写真"></div>
  <header class="site-header">
    <ul class="nav header-nav-left"><li class="en">HOME</li><li>施工実績</li><li>システム建築</li><li>リクルート</li></ul>
    <div class="brand">
      <div class="brand-tag">地域に愛される企業を目指す</div>
      <div class="brand-name"><span class="brand-mark"></span>椿ビルズ株式会社</div>
    </div>
    <div class="tel"><small>TEL</small>028-555-0147</div>
    <ul class="nav header-nav-right"><li class="en">CSR</li><li>会社案内</li><li>お問い合わせ</li></ul>
  </header>
  <div class="hero-copy">
    <h1>私たちは作っている</h1>
    <p>道路、橋梁、建物をはじめとした暮らしの基盤を、ひとつひとつ丁寧に造り続けています。地域の未来を支える仕事です。</p>
  </div>
</section>

<section class="info">
  <div class="info-label en">INFORMATION</div>
  <div class="info-body"><span>2017.05.08</span>ここに最新のお知らせが入ります</div>
  <div class="info-btn en">MORE</div>
</section>

<section class="grid">
  <div class="cell photo" role="img" aria-label="ヘルメット姿の社員の写真" style="background:linear-gradient(120deg,#cfd6dc,#8d9aa3 60%,#5f6e78)"></div>
  <div class="cell panel">
    <div class="panel-label en">ABOUT US</div>
    <div class="panel-title">椿ビルズとは</div>
    <div class="more en">MORE</div>
  </div>

  <div class="cell panel">
    <div class="panel-lead">私達が作り上げてきたもの</div>
    <div class="panel-label en">WORKS</div>
    <div class="panel-title">施工実績</div>
    <div class="more en">MORE</div>
  </div>
  <div class="cell photo" role="img" aria-label="施工した建物と夜景の写真コラージュ" style="background:linear-gradient(135deg,#1d3f7a,#6c86a8 50%,#b9c3c9)"></div>

  <div class="cell photo" role="img" aria-label="青空の下に建つ倉庫の写真" style="background:linear-gradient(180deg,#5fa6e0 0%,#a9d1f1 45%,#e6e6e2 60%,#b9b8b0)"></div>
  <div class="cell panel">
    <div class="panel-lead">施工・基礎・物流・工場</div>
    <div class="panel-label en">SYSTEM BUILDING</div>
    <div class="panel-title">システム建築</div>
    <div class="more en">MORE</div>
  </div>

  <div class="cell panel">
    <div class="panel-lead">未来の作手をつくる仕事</div>
    <div class="panel-label en">RECRUIT</div>
    <div class="panel-title">採用情報</div>
    <div class="more en">MORE</div>
  </div>
  <div class="cell photo" role="img" aria-label="現場で打ち合わせをする社員の写真" style="background:linear-gradient(120deg,#e9ecef,#9fb0bb 55%,#55656e)"></div>

  <div class="cell tall photo" role="img" aria-label="森の中で作業する人々の写真" style="background:linear-gradient(160deg,#4e6b33,#7c8f4d 50%,#3c4a25)"></div>
  <div class="cell tall panel">
    <div class="panel-lead">地域とともに歩んでいます</div>
    <div class="panel-label en">CORPORATE SOCIAL RESPONSIBILITY</div>
    <div class="panel-title en">CSR</div>
    <div class="more en">MORE</div>
  </div>
</section>

<section class="access">
  <div class="sec-head">
    <div class="en">ACCESS</div>
    <h2>アクセスマップ</h2>
  </div>
  <div class="map" role="img" aria-label="本社周辺の地図"></div>
  <div class="access-foot">
    <span>〒320-0099 みどり県つばき市中央3-10-18</span>
    <span class="btn-dark">大きな地図で見る</span>
  </div>
</section>

<section class="chara">
  <div class="sec-head">
    <div class="en">OFFICIAL CHARACTER</div>
    <h2>公式イメージキャラクター</h2>
  </div>
  <div class="chara-banner">
    <div class="chara-a" role="img" aria-label="黄色背景の公式キャラクターのイラスト"></div>
    <div class="chara-b" role="img" aria-label="ピンク背景の公式キャラクターのイラスト"></div>
  </div>
  <div class="more en">MORE</div>
</section>

<footer class="site-footer">
  <nav class="foot-nav">
    <ul><li class="en">HOME</li></ul>
    <ul><li>施工実績</li><li>道路</li><li>土木</li><li>建物</li><li>地域の主な実績</li></ul>
    <ul><li>システム建築</li><li>施工事例</li><li>構造システム建築</li><li>よくある質問</li></ul>
    <ul><li>リクルート</li></ul>
    <ul><li class="en">CSR</li></ul>
    <ul><li>会社案内</li></ul>
    <ul><li>お問い合わせ</li></ul>
  </nav>
  <div class="foot-brand">
    <div class="brand-tag" style="font-size:11px">地域に愛される企業を目指す</div>
    <div class="brand-name"><span class="brand-mark"></span>椿ビルズ株式会社</div>
    <div class="tel-foot"><small style="font-size:15px">TEL</small> 028-555-0147</div>
  </div>
  <div class="copy en">Copyright © TSUBAKI BUILDS Co.,Ltd. All Rights Reserved.</div>
</footer>

</body>
</html>
```